50-60's Rock singer' 'Only a voice and a song' show add for poster etc

The singer's name is Dewey Hart.

He is the only one of the 3 major superstars of the late 50's early 60's original Rock'n'Roll era who still performing. He is 'The Last man standing from his era'. and this show is called, 'Only a voice and a song'.

The show is a one man show where he sings his own Gold Hits, tells stories about his career and sings the biggest hits of that era, that his friends recorded.
It also features a special a special Audio Visual show to relive the 50's and 60's.
Up until this show, the well known singer had always performed with his band, so there may be an expectation that they will be here on this show.

There is no band however the music featured is the best Rock'n'Roll available.
I'd be interested in seeing your initial ideas so we can work through them.
I don't see it as being too busy although I am open to suggestions.
Just some photos attached but many other available.
You can Searcha and Vidstream his name if you need more info.
Updates

Hi guys, Update. Sorry, but somehow the singer's name was left out of the brief.. It is Dewey Hart. Many thanks for the ideas thus far. You are all very talented. I have attached some more photos and a couple of ideas that have been used with Carlo and Benny images.

Target Market(s)

Theatres. clubs, demographic 55 up - Rockabilly, Fifties Rock'n'Roll (Early Carlo era)

Industry/Entity Type

Entertainment

Requirements
Must have
• Dewey Hart -name, Last man Standing from his era - sub title, Only a voice and a song -show title
Nice to have
• The ideas of the Carlo and Benny images are nice and could be used. If the image in the blue shirt (20220325_111431-cropped.jpg) is used, thicken the hair so one cannot see through it.
Should not have
• NO dates, times, venues etc

```html
<!DOCTYPE html>
<html lang="en">
<head>
<meta charset="utf-8">
<title>Dewey Hart – Only a voice and a song</title>
<link rel="stylesheet" href="https://fonts.googleapis.com/css2?family=Baloo+2:wght@800&family=Montserrat:wght@700&family=Paytone+One&family=Sacramento&display=swap">
<style>
  :root {
    --ink: #000000;
    --cream: #f8ecc0;
    --sepia-light: #cfc29a;
    --sepia-mid: #6d6651;
    --red: #a8281b;
    --red-dark: #8e2016;
    --gold: #e2c47a;
    --ribbon-shadow: #4a4a3c;
  }
  html, body {
    margin: 0;
    padding: 0;
    background: var(--ink);
    overflow: hidden;
  }
  .poster {
    position: relative;
    width: 783px;
    height: 1200px;
    background: var(--ink);
    overflow: hidden;
  }
  .poster p, .poster h1, .poster h2 { margin: 0; }

  .singer-photo {
    position: absolute;
    left: 0;
    top: 0;
    width: 783px;
    height: 900px;
    background:
      radial-gradient(ellipse 260px 360px at 200px 420px, var(--sepia-light) 0%, var(--sepia-mid) 45%, rgba(0,0,0,0) 100%),
      radial-gradient(ellipse 140px 160px at 60px 700px, var(--sepia-mid) 0%, rgba(0,0,0,0) 100%),
      radial-gradient(ellipse 220px 200px at 640px 760px, #3a372c 0%, rgba(0,0,0,0) 100%);
  }
  .guitar-illustration {
    position: absolute;
    left: 478px;
    top: 104px;
    width: 120px;
    height: 520px;
    border-radius: 40px 40px 60px 60px;
    background: linear-gradient(180deg, var(--red) 0%, var(--red-dark) 100%);
  }

  .show-title {
    position: absolute;
    left: 425px;
    top: 172px;
    width: 265px;
    font-family: "Baloo 2", sans-serif;
    font-weight: 800;
    color: var(--cream);
    text-align: center;
    white-space: nowrap;
  }
  .show-title span { display: block; }
  .show-title .t-top  { font-size: 70px;  line-height: 84px; }
  .show-title .t-main { font-size: 106px; line-height: 112px; letter-spacing: -2px; }
  .show-title .t-mid  { font-size: 80px;  line-height: 92px; }
  .show-title .t-end  { font-size: 96px;  line-height: 104px; }

  .tagline {
    position: absolute;
    left: 0;
    top: 856px;
    width: 783px;
    height: 46px;
    line-height: 46px;
    text-align: center;
    font-family: "Sacramento", cursive;
    font-size: 44px;
    color: var(--cream);
  }

  .banner {
    position: absolute;
    left: 103px;
    top: 918px;
    width: 577px;
    height: 76px;
  }
  .banner svg { position: absolute; left: 0; top: 0; }
  .banner-text {
    position: absolute;
    left: 36px;
    top: 2px;
    width: 505px;
    height: 54px;
    line-height: 54px;
    text-align: center;
    font-family: "Montserrat", sans-serif;
    font-weight: 700;
    font-size: 30px;
    color: var(--red);
  }

  .era {
    position: absolute;
    left: 0;
    top: 1016px;
    width: 783px;
    height: 44px;
    line-height: 44px;
    text-align: center;
    font-family: "Montserrat", sans-serif;
    font-weight: 700;
    font-size: 34px;
    color: var(--cream);
  }
  .artist-name {
    position: absolute;
    left: 0;
    top: 1066px;
    width: 783px;
    height: 64px;
    line-height: 64px;
    text-align: center;
    font-family: "Paytone One", sans-serif;
    font-weight: 400;
    font-size: 66px;
    letter-spacing: 1px;
    color: var(--red);
  }
  .subtitle {
    position: absolute;
    left: 0;
    top: 1146px;
    width: 783px;
    height: 26px;
    line-height: 26px;
    text-align: center;
    font-family: "Montserrat", sans-serif;
    font-weight: 700;
    font-size: 18px;
    letter-spacing: 3px;
    color: var(--cream);
  }
</style>
</head>
<body>
<main class="poster">
  <div class="singer-photo" role="img" aria-label="Sepia photograph of the singer in profile, singing into a microphone"></div>
  <div class="guitar-illustration" role="img" aria-label="Red electric guitar illustration with radiating lines behind the show title"></div>

  <h1 class="show-title">
    <span class="t-top">Only a</span>
    <span class="t-main">voice</span>
    <span class="t-mid">and a</span>
    <span class="t-end">song</span>
  </h1>

  <p class="tagline">Stories, Hits and Memories</p>

  <div class="banner">
    <svg width="577" height="76" viewBox="0 0 577 76" aria-hidden="true">
      <polygon points="0,50 36,24 36,72" fill="var(--gold)"/>
      <polygon points="577,50 541,24 541,72" fill="var(--gold)"/>
      <polygon points="36,56 82,56 82,72 36,72" fill="var(--ribbon-shadow)"/>
      <polygon points="495,56 541,56 541,72 495,72" fill="var(--ribbon-shadow)"/>
      <rect x="36" y="2" width="505" height="54" fill="var(--cream)"/>
    </svg>
    <div class="banner-text">AN AUDIO VISUAL EVENT</div>
  </div>

  <p class="era">1950-1960 ORIGINAL</p>
  <h2 class="artist-name">DEWEY HART</h2>
  <p class="subtitle">LAST MAN STANDING FROM HIS ERA</p>
</main>
</body>
</html>
```